Flyer-Design für Rücken-Massage, Klangtherapie etc.
Sehr kompetent und schnelle Umsetzung, gute Gestaltung, Farblich in Harmonie. Schnelle Änderungen, bin sehr zufrieden. Danke für die super Arbeit.
Zielgruppe
Rücken-Massage, Klangtherapie, Fußreflex-Massage, Quantenheilung
Aufgabenstellung
Text zu den Rubriken können vom Internet entnommen werden.
https://wohlruhe-tonpraxis.ch/

```html
<!DOCTYPE html>
<html lang="de">
<head>
<meta charset="utf-8">
<title>Wohlruhe-Tonpraxis – Rücken-Nackenmassage</title>
<link href="https://fonts.googleapis.com/css2?family=Montserrat:wght@400;700&display=swap" rel="stylesheet">
<style>
  :root {
    --brand-green: #8cc63f;
    --band-green: #b9c15a;
    --ink: #1a1a1a;
    --paper: #ffffff;
    --photo-massage: linear-gradient(135deg, #3f6b22 0%, #8aa65a 45%, #e9d8c8 75%, #f4f4f2 100%);
    --photo-portrait: linear-gradient(160deg, #5f8a3a 0%, #8fae5e 40%, #d9b48a 60%, #b8503a 100%);
  }
  * { margin: 0; padding: 0; box-sizing: border-box; }
  html, body {
    width: 846px; height: 1200px; overflow: hidden;
    background: var(--paper);
  }
  .flyer {
    position: relative; width: 846px; height: 1200px;
    font-family: "Montserrat", sans-serif; color: var(--ink);
    background: var(--paper);
  }
  .brand {
    position: absolute; left: 328px; top: 30px;
    display: flex; align-items: center; gap: 12px;
    color: var(--brand-green); font-weight: 400;
  }
  .brand-mark {
    width: 76px; height: 76px; border-radius: 50%;
    background: var(--brand-green); flex: none;
  }
  .brand-name { font-size: 29px; line-height: 1.1; letter-spacing: -0.2px; }
  .brand-name small { display: block; font-size: 23px; font-weight: 400; }

  .section-title {
    font-weight: 700; font-size: 23px; line-height: 28px; text-align: center;
  }
  .massage-title { position: absolute; left: 0; width: 846px; top: 154px; }
  .body-copy {
    font-size: 16px; line-height: 21.8px;
    text-align: justify; hyphens: manual;
  }
  .massage-intro { position: absolute; left: 101px; width: 655px; top: 196px; }
  .effects {
    position: absolute; left: 101px; width: 310px; top: 327px;
    font-size: 16px; line-height: 21.8px; list-style: none;
  }
  .photo-massage {
    position: absolute; left: 445px; top: 343px; width: 295px; height: 186px;
    background: var(--photo-massage);
  }
  .about-title { position: absolute; left: 73px; width: 239px; top: 609px; }
  .photo-portrait {
    position: absolute; left: 73px; top: 656px; width: 238px; height: 231px;
    background: var(--photo-portrait);
  }
  .about-copy { position: absolute; left: 334px; width: 440px; top: 615px; }
  .about-copy p + p { margin-top: 21.8px; }

  .contact {
    position: absolute; left: 0; top: 939px; width: 846px; height: 261px;
    background: var(--band-green); text-align: center;
  }
  .contact .section-title { margin-top: 16px; margin-bottom: 6px; }
  .contact address {
    font-style: normal; font-size: 17px; line-height: 21.8px;
  }
</style>
</head>
<body>
<main class="flyer">
  <header class="brand">
    <span class="brand-mark"></span>
    <span class="brand-name">Wohlruhe-Tonpraxis<small>Marlene Hollmannsried</small></span>
  </header>

  <h1 class="section-title massage-title">Rücken-Nackenmassage</h1>
  <p class="body-copy massage-intro">Nacken-Schulter und Rückenverspannungen können gelöst werden Ge&shy;lenk-und Muskelschmerzen können dabei gelindert werden. Die Durch&shy;blutung wird dabei gefördert, das Hautbild verbessert, die Sauerstoff&shy;zufuhr im Blut wird vermehrt, der Stoffwechsel angereget, der Körper entgiftet und Schlackstoffe werden abtransportiert.</p>

  <ul class="effects">
    <li>Wirkungsweise:</li>
    <li>– steigert lokale Durchblutung</li>
    <li>– entspannt Haut, Bindegewebe und Muskulatur</li>
    <li>– löst Verklebungen und Narben</li>
    <li>– senkt Blutdruck und Pulsfre-<br>quenz</li>
    <li>– lindert Schmerzen</li>
    <li>– bringt psychische Entspannung</li>
    <li>– reduziert Stress</li>
  </ul>
  <div class="photo-massage" role="img" aria-label="Foto: Frau erhält eine entspannende Rückenmassage im Grünen"></div>

  <h2 class="section-title about-title">Über mich</h2>
  <div class="photo-portrait" role="img" aria-label="Porträtfoto der Therapeutin vor grünem Hintergrund"></div>
  <div class="body-copy about-copy">
    <p>Aufgewachsen bin ich in der Ostschweiz, wo ich zuerst eine Lehre als Buchbinderin abgeschlossen habe. Einige Jahre später besuchte ich verschiedene Weiter&shy;bildungen – Kurse, die mir die Möglichkeit gaben, neue Erfahrungen zu sammeln und im Bereich der Entspannung umzusetzen.</p>
    <p>Weil ich Neuem immer offen und mit Neugier begegnet bin, konnte ich all das Gelernte mit&shy;einander verbinden, um Menschen im Alltag zu mehr Ruhe und Wohlbefinden zu verhelfen und Körper und Geist in Harmonie und Einklang zu bringen.</p>
  </div>

  <footer class="contact">
    <h2 class="section-title">Kontakt</h2>
    <address>
      GEMEINSCHAFTS-PRAXIS<br>
      Marlene Hollmannsried<br>
      Lindenhofstrasse 14<br>
      4188 Lindwil BL<br>
      Telefon: 076 408 17 52<br>
      E-Mail: info@wohlruhe-tonpraxis.ch
    </address>
  </footer>
</main>
</body>
</html>
```